Law Firm Website

I currently have a temporary site that I created myself at www.kbrandellegal.net (hosted by hostpivot). I am generally happy with the content.

My permanent website just has basic information right now: www.kbrandellegal.com (hosted by cloudperch). I want to take the general content from the temporary website and have a more professional looking website on the permanent website. I want it in Wordpress format. I want a link to my blog: www.rivetsand.com. I want it to work on pads and smart phones. My number and e-mail address should be available on every page. The idea is to feature the potential client more than the lawyer.
Updates

Several of the designs are good. I would like the front page to have my number and address at the top (and at the top of every page) and to identify my law firm as "Law Office of Karen J. Brandell". No need to include "kbrandellegal" as that is just the web address. I like showing the most recent blog posts on the front page. I don't need video. No need to emphasize office hours or map location on the front page (that could be under a contact button). My picture should be somewhere. I would like an image from Boston on the front page if we can find one that is not copyright protected. No images of gavels or scales of justice. See some of the sample websites I listed in previous messages. Thanks!

Reason: I need more time to evaluate designs.

Reason: Designers apparently misunderstood and provided design that was not wordpress.

Industry/Entity Type

Law Firm

```html
<!DOCTYPE html>
<html lang="en">
<head>
<meta charset="utf-8">
<title>Law Office of Karen J. Brandell</title>
<link rel="stylesheet" href="https://fonts.googleapis.com/css2?family=Arimo:wght@400;700&display=swap">
<style>
:root{
  --accent:#0a8fbf;
  --ink:#555;
  --ink-soft:#777;
  --ink-light:#999;
  --ink-dark:#444;
  --page:#efefef;
  --white:#fff;
  --rule:#dcdcdc;
  --btn:#666;
}
*{box-sizing:border-box;margin:0;padding:0}
html,body{width:1200px;height:1000px;overflow:hidden}
body{font-family:"Arimo",Arial,sans-serif;background:var(--page);color:var(--ink);position:relative}
.site-header{position:absolute;left:0;top:0;width:1200px;height:100px;background:var(--white);border-bottom:1px solid var(--rule)}
.brand{position:absolute;left:255px;top:28px}
.brand-kicker{color:var(--accent);font-size:13px}
.brand-name{color:var(--ink-soft);font-size:26px;font-weight:700;margin-top:4px;letter-spacing:.2px}
.header-address{position:absolute;left:610px;top:28px;font-size:11px;color:var(--ink-soft);line-height:16.5px}
.header-address svg{position:absolute;left:0;top:2px}
.header-address p{padding-left:16px}
.header-contact{position:absolute;left:770px;top:28px;font-size:11px;color:var(--ink-soft);line-height:16.5px}
.header-contact li{list-style:none;position:relative;padding-left:18px}
.header-contact svg{position:absolute;left:0;top:3px}
.main-nav{position:absolute;left:255px;top:100px;width:682px;height:37px;display:flex;align-items:center}
.main-nav a{font-size:8px;color:var(--ink-soft);text-decoration:none;text-transform:uppercase;letter-spacing:.3px;padding:0 13px}
.main-nav a.active{background:var(--accent);color:var(--white);font-weight:700;height:37px;line-height:37px;width:66px;text-align:center;padding:0;margin-right:12px}
.hero{position:absolute;left:255px;top:137px;width:682px;height:290px;background:linear-gradient(100deg,#2a2019 0%,#4a3a2c 30%,#6f5d4a 55%,#9c8b78 75%,#3a3631 100%);box-shadow:0 6px 8px -4px rgba(0,0,0,.25)}
.hero-caption{position:absolute;left:30px;top:122px;color:var(--white)}
.hero-caption h1{font-size:20px;font-weight:400;letter-spacing:.3px}
.hero-caption p{font-size:14px;margin-top:5px}
.section-title{font-size:13px;color:var(--ink-dark);text-transform:uppercase;font-weight:400;letter-spacing:.3px}
.practice{position:absolute;left:255px;top:468px;width:210px}
.practice .sub{color:var(--accent);font-size:9px;text-transform:uppercase;margin-top:7px}
.practice ul{list-style:none;margin-top:18px}
.practice li{font-size:9.5px;color:var(--ink);padding-left:13px;position:relative;height:21.5px}
.practice li::before{content:"»";position:absolute;left:0;top:-1px;color:var(--ink-light)}
.portrait{position:absolute;left:485px;top:471px;width:176px;height:121px;background:linear-gradient(135deg,#e4e4e4,#c9c9c9)}
.welcome{position:absolute;left:682px;top:468px;width:256px}
.welcome p{font-size:8.3px;color:var(--ink-soft);line-height:13.5px;margin-top:17px}
.btn{display:inline-block;background:var(--btn);color:var(--white);font-size:7px;font-weight:700;text-transform:uppercase;text-align:center;line-height:27px;height:27px;border-radius:2px;letter-spacing:.3px}
.welcome .btn{width:77px;margin-top:15px}
.panel{position:absolute;left:255px;top:627px;width:682px;height:274px;background:var(--white)}
.blog{position:absolute;left:26px;top:24px;width:155px}
.post{margin-top:22px;padding-bottom:12px;border-bottom:1px solid #e6e6e6}
.post+.post{margin-top:12px;border-bottom:none}
.post .meta{color:var(--accent);font-size:8px}
.post .title{color:var(--ink-soft);font-size:8px;font-weight:700;line-height:12.5px;margin-top:7px}
.blog .btn{position:absolute;top:190px;left:0;width:91px}
.advice{position:absolute;left:229px;top:24px;width:430px}
.advice .lead{position:absolute;top:37px;left:2px;width:250px;color:var(--accent);font-size:8.5px;line-height:11.5px}
.advice .body{position:absolute;top:92px;left:2px;width:255px;color:var(--ink-soft);font-size:8.5px;line-height:12px}
.advice-photo{position:absolute;left:497px;top:62px;width:162px;height:146px;background:linear-gradient(160deg,#3a4f7c 0%,#6d83a8 45%,#b9c6d8 70%,#5b5146 100%)}
.footer-nav{position:absolute;left:255px;top:919px;display:flex;font-size:7.5px;color:var(--ink-light)}
.footer-nav a{color:var(--ink-light);text-decoration:none;padding:0 8px;border-left:1px solid #ccc;line-height:13px}
.footer-nav a:first-child{padding-left:0;border-left:none}
.copyright{position:absolute;right:263px;top:921px;font-size:7.5px;color:var(--ink-soft)}
.site-footer{position:absolute;left:0;top:943px;width:1200px;height:57px;background:var(--white);border-top:1px solid var(--rule)}
.footer-brand{position:absolute;left:256px;top:13px;color:var(--ink-soft)}
.footer-brand span{display:block;font-size:8.5px}
.footer-brand strong{display:block;font-size:14px;font-weight:400;margin-top:3px}
.social{position:absolute;left:820px;top:13px;display:flex;gap:7px}
.social span{width:25px;height:25px;border-radius:3px;display:block}
.s1{background:#3b5a9a}.s2{background:#2fa8df}.s3{background:#333}.s4{background:#ee7d1f}
</style>
</head>
<body>
<header class="site-header">
  <div class="brand">
    <div class="brand-kicker">Law Office of</div>
    <div class="brand-name">Karen J. Brandell</div>
  </div>
  <div class="header-address">
    <svg width="8" height="11" viewBox="0 0 8 11"><path d="M4 0a4 4 0 0 0-4 4c0 3 4 7 4 7s4-4 4-7a4 4 0 0 0-4-4zm0 5.5A1.5 1.5 0 1 1 4 2.5a1.5 1.5 0 0 1 0 3z" fill="#888"/></svg>
    <p>48 Harlow St.<br>4th Floor<br>Boston, MA 02110</p>
  </div>
  <ul class="header-contact">
    <li><svg width="10" height="10" viewBox="0 0 10 10"><path d="M2 0l2 2.5-1 1.2c.6 1.3 1.5 2.2 2.8 2.8L7 5.5 9.5 7.5 8.5 9.5C4 9.5.5 6 .5 1.5z" fill="#888"/></svg>Phone: 617 555-0142</li>
    <li><svg width="11" height="10" viewBox="0 0 11 10"><rect x="2.5" y="0.5" width="6" height="3" fill="none" stroke="#888"/><rect x="0.5" y="3.5" width="10" height="4" fill="none" stroke="#888"/><rect x="2.5" y="6" width="6" height="3.5" fill="#fff" stroke="#888"/></svg>Fax: 857 555-0187</li>
    <li><svg width="11" height="8" viewBox="0 0 11 8"><rect width="11" height="8" fill="#888"/><path d="M0 0l5.5 4.5L11 0" fill="none" stroke="#fff" stroke-width="1"/></svg>Email: kbrandell@kbrandellegal.com</li>
  </ul>
</header>

<nav class="main-nav">
  <a class="active" href="#">Home</a>
  <a href="#">Why Hire Me?</a>
  <a href="#" style="padding:0 26px 0 22px">Success Stories</a>
  <a href="#" style="padding:0 17px">Practice Area</a>
  <a href="#" style="padding:0 13px 0 18px">Representative Clients</a>
  <a href="#" style="padding:0 12px">Services Provided</a>
  <a href="#">Contact Us</a>
</nav>

<section class="hero" role="img" aria-label="Close-up of a hand signing a document with a fountain pen">
  <div class="hero-caption">
    <h1>WE ARE COMMITED</h1>
    <p>to understanding the Client’s Objectives!</p>
  </div>
</section>

<section class="practice">
  <h2 class="section-title">Practice &amp; Experience</h2>
  <div class="sub">Our Specializations</div>
  <ul>
    <li>Employment Counseling and Litigation</li>
    <li>Business Litigation</li>
    <li>Litigation Avoidance</li>
    <li>Businesss partner/shareholder Disputes.</li>
  </ul>
</section>

<div class="portrait" role="img" aria-label="Portrait of the attorney"></div>

<section class="welcome">
  <h2 class="section-title">Welcome to my website !</h2>
  <p>I don't do everything.&nbsp; I don't handle personal injury claims, criminal matters, divorces, real estate transactions, bankruptcies, etc. (I can refer you to excellent lawyers who do these things).&nbsp; I would rather be great at a few things than okay, or worse, at everything.</p>
  <a class="btn" href="#">[ Read More ]</a>
</section>

<section class="panel">
  <div class="blog">
    <h2 class="section-title">Recent Blog’s</h2>
    <article class="post">
      <div class="meta">January 15, 2014 in Lawsuits</div>
      <div class="title">You're Damned If You Don't Respond Appropriately to a Poor Rately Review or Online Post.</div>
    </article>
    <article class="post">
      <div class="meta">January 3, 2014 in Discrimination, Lawsuits</div>
      <div class="title">You're Damned if You Don't Settle Meri-torious Discrimination Cases</div>
    </article>
    <a class="btn" href="#">[ View All Blogs ]</a>
  </div>
  <div class="advice">
    <h2 class="section-title">We offer our clients an expert legal advice</h2>
    <p class="lead">Protecting and Defending Your Business Against Competitors, Rogue Employees, Cheating Business Partners, Devious Contracting Parties, and Overzealous Government Agencies.</p>
    <p class="body">Your business is under constant attack.&nbsp; With more success, you become more of a target.&nbsp; Whether it's keeping you out of a lawsuit or defending one that you are already in (or pros-ecuting one when necessary), I'm here to help.</p>
  </div>
  <div class="advice-photo" role="img" aria-label="Glass office tower seen from below against a blue sky"></div>
</section>

<nav class="footer-nav">
  <a href="#">Home</a><a href="#">Why Hire Me?</a><a href="#">Success Stories</a><a href="#">Practice Area</a><a href="#">Representative Clients</a><a href="#">Services Provided</a><a href="#">Contact Us</a>
</nav>
<div class="copyright">2014 © Law office of Karen J. Brandell</div>

<footer class="site-footer">
  <div class="footer-brand"><span>Law Office of</span><strong>Karen J. Brandell</strong></div>
  <div class="social">
    <span class="s1" role="img" aria-label="Social link"></span>
    <span class="s2" role="img" aria-label="Social link"></span>
    <span class="s3" role="img" aria-label="Social link"></span>
    <span class="s4" role="img" aria-label="Feed link"></span>
  </div>
</footer>
</body>
</html>
```